Banner design for an online shop

We need a banner for our online shop www.velmora-shop.de
This should be displayed on the start page in the carousel.
The banner should have the following dimensions: 1420 x 424 px

```html
<!DOCTYPE html>
<html lang="de">
<head>
<meta charset="utf-8">
<title>Mobiler Strom – Stromerzeuger</title>
<link rel="stylesheet" href="https://fonts.googleapis.com/css2?family=Open+Sans:wght@300;400;700;800&display=swap">
<style>
  :root {
    --bg-blue-dark: #1d3f8f;
    --bg-blue-mid: #2d56b0;
    --bg-blue-light: #4470c6;
    --panel-dark: #0f1d2e;
    --panel-light: #ffffff;
    --accent: #4aa8ec;
    --text-white: #ffffff;
    --text-accent: #4aa6ea;
    --side-label: #d8d8d8;
  }
  * { margin: 0; padding: 0; box-sizing: border-box; }
  html, body { width: 1200px; height: 358px; overflow: hidden; }
  body { font-family: "Open Sans", Arial, sans-serif; }

  .banner {
    position: relative;
    width: 1200px;
    height: 358px;
    overflow: hidden;
  }
  .banner__backdrop {
    position: absolute;
    inset: 0;
    background:
      radial-gradient(ellipse at 20% 30%, var(--bg-blue-light) 0%, transparent 55%),
      radial-gradient(ellipse at 85% 80%, var(--bg-blue-light) 0%, transparent 50%),
      linear-gradient(120deg, var(--bg-blue-mid), var(--bg-blue-dark) 60%, var(--bg-blue-mid));
  }
  .banner__card-light {
    position: absolute;
    left: 593px; top: 15px;
    width: 510px; height: 330px;
    background: var(--panel-light);
    border-radius: 8px;
  }
  .banner__side-label {
    position: absolute;
    left: 1066px; top: 180px;
    transform: translate(-50%, -50%) rotate(-90deg);
    white-space: nowrap;
    font-weight: 800;
    font-size: 33px;
    letter-spacing: 0.5px;
    color: var(--side-label);
  }
  .banner__card-dark {
    position: absolute;
    left: 106px; top: 28px;
    width: 773px; height: 303px;
    background: var(--panel-dark);
    border-radius: 8px;
  }
  .banner__title {
    position: absolute;
    left: 163px; top: 78px;
    font-weight: 700;
    font-size: 52px;
    line-height: 1;
    color: var(--text-white);
    white-space: nowrap;
  }
  .banner__subtitle {
    position: absolute;
    left: 165px; top: 158px;
    font-weight: 300;
    font-size: 52px;
    line-height: 1;
    color: var(--text-accent);
    white-space: nowrap;
  }
  .banner__button {
    position: absolute;
    left: 171px; top: 241px;
    width: 182px; height: 55px;
    border-radius: 28px;
    background: var(--accent);
    display: flex;
    align-items: center;
    justify-content: space-between;
    padding: 0 3px 0 27px;
    color: var(--text-white);
    font-weight: 700;
    font-size: 13px;
    text-decoration: none;
  }
  .banner__button-icon {
    width: 49px; height: 49px;
    border-radius: 50%;
    background: var(--panel-light);
    display: flex;
    align-items: center;
    justify-content: center;
  }
  .banner__product {
    position: absolute;
    left: 659px; top: 55px;
    width: 376px; height: 266px;
    border-radius: 14px;
    background: linear-gradient(135deg, #2a3fa8 0%, #1f2f8a 45%, #15161c 100%);
  }
</style>
</head>
<body>
  <section class="banner">
    <div class="banner__backdrop" role="img" aria-label="Blau eingefärbtes Hintergrundfoto mit Werkzeugen"></div>
    <div class="banner__card-light">
    </div>
    <span class="banner__side-label">MOBILER STROM</span>
    <div class="banner__card-dark"></div>
    <h1 class="banner__title">MOBILER STROM</h1>
    <h2 class="banner__subtitle">STROMERZEUGER</h2>
    <a class="banner__button" href="#">
      <span>MEHR INFOS</span>
      <span class="banner__button-icon">
        <svg width="14" height="12" viewBox="0 0 14 12" aria-hidden="true">
          <path d="M1 1l5 5-5 5M7 1l5 5-5 5" fill="none" stroke="#4aa8ec" stroke-width="2" stroke-linecap="round" stroke-linejoin="round"/>
        </svg>
      </span>
    </a>
    <div class="banner__product" role="img" aria-label="Produktfoto: blauer Benzin-Stromerzeuger mit schwarzem Rohrrahmen"></div>
  </section>
</body>
</html>
```